Business Card Design

We need business cards designed incorporating our graphics/logo already used on our trucks. We are a small construction company that does everything from building new homes, additions, Kitchens, Baths, Decks, Hardwood Floors/Tile, all phases of construction. No job is too small. We pride ourselves on True Craftmanship/Customer Satisfaction, its what truly separates us from everyone else.

Industry/Entity Type

Construction

Contact Information for Business Card

Maple Ridge Renovations Lic#27KT51986400
342 51st Avenue Sea Isle City NJ 08243
(555)317-2984 Email: info@mapleridgellc.example
Paul Tremondale

```html
<!DOCTYPE html>
<html lang="en">
<head>
<meta charset="utf-8">
<title>Maple Ridge Renovations – Business Card</title>
<link href="https://fonts.googleapis.com/css2?family=Arimo:wght@400;700&display=swap" rel="stylesheet">
<style>
  :root {
    --page: #eef1f3;
    --card-front: #d6eef7;
    --card-back: #eaf5f9;
    --sky-top: #bfe3f2;
    --tan-strip: #dcc08c;
    --ink: #111111;
    --ink-soft: #2b2b2b;
    --white: #ffffff;
    --navy: #124f8f;
  }
  * { margin: 0; padding: 0; box-sizing: border-box; }
  html, body { width: 1200px; height: 767px; overflow: hidden; }
  body {
    background: var(--page);
    font-family: "Arimo", Arial, sans-serif;
    position: relative;
  }

  /* ---------- Front of card ---------- */
  .card-front {
    position: absolute;
    left: 255px; top: 97px;
    width: 490px; height: 283px;
    background: linear-gradient(180deg, var(--sky-top) 0%, var(--card-front) 60%);
    overflow: hidden;
    box-shadow: 0 6px 18px rgba(0,0,0,.18);
  }
  .logo-area {
    position: absolute;
    left: 0; top: 0;
    width: 386px; height: 283px;
    display: flex;
    align-items: center;
    justify-content: center;
  }
  .brand-name {
    text-align: center;
    font-weight: 700;
    font-size: 40px;
    line-height: 50px;
    color: var(--ink-soft);
    letter-spacing: 1px;
    text-transform: uppercase;
  }
  .license-strip {
    position: absolute;
    left: 386px; top: 0;
    width: 104px; height: 283px;
    background: var(--tan-strip);
  }
  .license-strip span {
    position: absolute;
    left: 50%; top: 50%;
    transform: translate(-50%, -50%) rotate(90deg);
    white-space: nowrap;
    font-weight: 700;
    font-size: 18px;
    letter-spacing: .5px;
    color: var(--ink);
  }

  /* ---------- Back of card ---------- */
  .card-back {
    position: absolute;
    left: 420px; top: 440px;
    width: 462px; height: 215px;
    background: var(--card-back);
    overflow: hidden;
    box-shadow: 0 6px 18px rgba(0,0,0,.18);
  }
  .name-bar {
    position: absolute;
    left: 0; top: 0;
    width: 100%; height: 28px;
    background: var(--tan-strip);
  }
  .person-name {
    position: absolute;
    left: 210px; top: 4px;
    font-weight: 700;
    font-size: 17px;
    color: var(--ink);
  }
  .mini-logo {
    position: absolute;
    left: 17px; top: 55px;
    width: 178px; height: 127px;
    display: flex;
    align-items: center;
    justify-content: center;
  }
  .mini-name {
    text-align: center;
    font-weight: 700;
    font-size: 16px;
    line-height: 21px;
    color: var(--ink-soft);
    text-transform: uppercase;
  }
  .contact {
    position: absolute;
    left: 211px; top: 50px;
    font-size: 14px;
    line-height: 16px;
    color: var(--ink);
  }
  .contact p { margin-bottom: 2px; }
  .contact .row { display: flex; align-items: flex-start; gap: 6px; margin-top: 4px; }
  .contact .row svg { flex: none; margin-top: 1px; }
  .services-bar {
    position: absolute;
    left: 0; top: 192px;
    width: 100%; height: 23px;
    background: var(--navy);
    color: var(--white);
    font-size: 12.5px;
    line-height: 23px;
    text-align: center;
  }
</style>
</head>
<body>

<section class="card-front" aria-label="Front of business card">
  <div class="logo-area">
    <h1 class="brand-name">Maple Ridge<br>Renovations</h1>
  </div>
  <div class="license-strip"><span>LIC#27KT51986400</span></div>
</section>

<section class="card-back" aria-label="Back of business card">
  <div class="name-bar"><span class="person-name">Paul Tremondale</span></div>

  <div class="mini-logo">
    <div class="mini-name">Maple Ridge<br>Renovations</div>
  </div>

  <div class="contact">
    <p>Maple Ridge Renovations</p>
    <p>Lic#27KT51986400</p>
    <div class="row">
      <svg width="12" height="14" viewBox="0 0 12 14"><path d="M6 0a5 5 0 0 0-5 5c0 4 5 9 5 9s5-5 5-9a5 5 0 0 0-5-5zm0 7a2 2 0 1 1 0-4 2 2 0 0 1 0 4z" fill="#111"/></svg>
      <span>342 51st Avenue Sea Isle City<br>NJ 08243</span>
    </div>
    <div class="row">
      <svg width="12" height="14" viewBox="0 0 12 14"><circle cx="6" cy="7" r="6" fill="#111"/><path d="M4 4 l1.5 0 l.6 2 -1 .8 a5 5 0 0 0 2 2 l.8-1 2 .6 0 1.5 a1 1 0 0 1-1 1 A6 6 0 0 1 3 5 a1 1 0 0 1 1-1z" fill="#fff"/></svg>
      <span>(555)317-2984</span>
    </div>
    <div class="row">
      <svg width="13" height="14" viewBox="0 0 13 14"><rect x="1" y="3" width="11" height="8" fill="none" stroke="#111" stroke-width="1.4"/><path d="M1 3 L6.5 8 L12 3" fill="none" stroke="#111" stroke-width="1.4"/></svg>
      <span>info@mapleridgellc.example</span>
    </div>
  </div>

  <div class="services-bar">Kitchens | Baths | Decks | Hardwood Floors | All Phases of Construction.</div>
</section>

</body>
</html>
```